Designing a new homepage for www.Brindlework.net

WEBSITE: www.brindlework.net

ABOUT THE WEBSITE
The Brindlework.net (BWK) website contains a large directory of over 50,000 international trade service providers that is not valued enough on the homepage (HP). Currently from the HP, the site appears as a general site about imports and exports (international trade). As a result, it contradicts the purpose and experience of the site.
The website is new and original for international trade online: it is a tool to find the best experts and professionals that can help importers and exporters to implement their overseas operations.

Specifically:
a) An exporter who wants to sell in Italy can find on BWK: agents to distribute their products, a lawyer for reviewing contracts, translators to translate brochures and websites, an export consultant, etc. Various local providers that can help sell their products in Italy, a local provider (e.g. based in Italy) are generally more efficient and less costly than a supplier in the exporter’s home country

b) An importer who wants to buy in China will find purchasing agents who source products for third parties; logistics companies that store and ship merchandise; corporate quality control to ensure product quality before shipment, etc.; various local providers based in China to better organize its import operation.

BWK is therefore a very resourceful solution for SMEs who want to develop, improve and organize their international trade:
a) it significantly increases their ability to create new opportunities by using the services of a third party: export to a new country; import a new product
b) it allows them to optimize their purchases of services by seeking alternatives: find a less expensive carrier, a foreign lawyer challenged by a local lawyer

It is the perfect complement to cross border marketplaces (e.g. Quorvanta.com, fenwickmarts.com, zl48.com) which concentrate on the search for products (and of companies/counterparts) but:
a) help the user to import only, not really export
b) do not help implement the operations of exporting/importing from A to Z

Therefore, BWK offers a new way of “easy exporting” (or easy importing).

THE BRIEF

The objective of the project is to rethink the HP (and the site design) to highlight this experience: "export and import more successfully through 50,000+ service providers in over 100 countries”.
We have created a wireframe (see attached) of the structure we feel best meets this objective. What do you think? Do we meet it through our wireframe? Then, next step is to take this wireframe and create a clear design that really helps us to achieve our objective.

It is considered that the site captures the importers/exporters seeking to increase their exports or to better organize their imports (but we do not start from a priori that these users are looking for service providers).
The HP should highlight the importance of service providers addressing export markets or better organizing their imports; the "market analyses" of the site should act as a "knowledge resource", where the site offers more the main experience: if you want to export to a country you have any interest to first explore what the partners listed by BWK can provide.

Reason: We feel that we're seeing some interesting designs and would like to give current and even potential submissions more time. So far we have not seen the one that really strikes us, so perhaps more time is what we and the designers need! Thanks!

Target Market(s)

Importers, exporters, international trade service providers, foreign investors, etc

Industry/Entity Type

Lawyer

Requirements
Must have
• • Please use the current basic design elements of the website, including the logo, (www.brindlework.net). These include colors and fonts, etc. We only aim to change the HP and therefore, only implement a change to the header and footer of the whole site.
• Please find inspiration from our wireframes (attached), as they have been carefully thought about by our own team. However, should you feel the need to challenge the wireframes, please do so in your design, we're interested to see what you can present us.
• Our prime objective in terms of design: creating a more user-friendly interface on the HP to guide users into the rest of the website
• We already have a psd file based on the wireframes we’ve attached to the brief. If you would like this, so your job is easier (such as using same text as we have in the wireframes), let us know!

```html
<!DOCTYPE html>
<html lang="en">
<head>
<meta charset="utf-8">
<title>Brindlework.net – Home</title>
<link rel="stylesheet" href="https://fonts.googleapis.com/css2?family=Arimo:ital,wght@0,400;0,700;1,400&family=Archivo+Narrow:wght@500&display=swap">
<style>
:root{
  --page:#ffffff;
  --sidebar:#f8f8f8;
  --sidebar-line:#cfcfcf;
  --panel-a:#e2ded6;
  --panel-b:#d5cfc2;
  --divider:#bdb6a8;
  --divider-light:#eeeae2;
  --text:#555555;
  --text-soft:#6a6a6a;
  --heading:#6b6b6b;
  --ink:#222222;
  --link:#3d8fd8;
  --button:#e5e0d4;
  --button-line:#bfb8a8;
  --cta-top:#4ab0ee;
  --cta-bottom:#2288d2;
  --rule:#a9a9a9;
  --partner:#8a8a8a;
}
*{box-sizing:border-box;margin:0;padding:0}
html,body{width:1200px;height:900px;overflow:hidden;background:var(--page)}
body{position:relative;font-family:"Arimo",Arial,sans-serif;color:var(--text)}
a{color:var(--link)}
.abs{position:absolute}

/* sidebar */
.services{position:absolute;left:123px;top:-20px;width:284px;height:764px;background:var(--sidebar);border:1px solid var(--sidebar-line);border-top:none}
.services ul{list-style:none;position:absolute;left:15px;top:7px}
.services li{font-size:13px;line-height:26px;height:26px;padding-left:17px;position:relative;color:var(--text)}
.services li::before{content:"";position:absolute;left:1px;top:11px;width:5px;height:5px;border-radius:50%;background:#777}
.services li.group-start{margin-top:4px}
.services .all{position:absolute;left:180px;top:730px;font-size:11px;color:var(--text);text-decoration:underline}

/* main panel */
.panel{position:absolute;left:407px;top:0;width:668px;height:744px;background:linear-gradient(90deg,var(--panel-a),var(--panel-b))}
.rule-h{position:absolute;height:1px;background:var(--divider);box-shadow:0 1px 0 var(--divider-light)}
.quote{position:absolute;left:437px;width:300px;font-style:italic;font-size:13px;line-height:18px;color:var(--text-soft)}
.zone{position:absolute;left:437px;top:146px;width:85px;height:84px;background:#fff;border:1px solid #aaa}
.zone span{position:absolute;left:0;right:0;top:33px;text-align:center;font-size:14px;color:#444;background:rgba(255,255,255,.85)}
.speaker-name{left:534px;top:172px;font-size:12px;font-weight:700;color:var(--link)}
.speaker-role{left:534px;top:186px;font-size:13px;font-weight:700;color:#444}
.speaker-place{left:534px;top:206px;font-size:14px;color:var(--text-soft)}
.small-link{font-size:11px;text-decoration:underline;color:var(--link)}
.btn{position:absolute;display:flex;align-items:center;justify-content:center;font-family:"Archivo Narrow",Arial,sans-serif;font-weight:500;font-size:12px;color:#222;background:linear-gradient(#efebe2,var(--button));border:1px solid var(--button-line);box-shadow:0 1px 2px rgba(0,0,0,.15)}
.btn-cta{color:#fff;background:linear-gradient(var(--cta-top),var(--cta-bottom));border:1px solid #1b77bb}

/* provider cards */
.card-logo{position:absolute;left:772px;width:85px;height:85px;background:#fff;border:1px solid #c8c2b5;display:flex;align-items:center;justify-content:center;text-align:center;font-size:11px;font-weight:700;color:#666;padding:6px;line-height:14px}
.card-title{position:absolute;left:863px;font-size:12px;font-weight:700;color:var(--link)}
.card-sub{position:absolute;left:863px;font-size:11px;font-weight:700;color:#444}
.card-desc{position:absolute;left:864px;width:205px;font-size:11px;line-height:12px;color:var(--text)}
.card-profile{position:absolute;left:997px}

.free{position:absolute;left:770px;width:300px;text-align:center;font-size:18px;font-weight:700;line-height:23px;color:#777}

/* tips */
.section-title{position:absolute;font-size:16px;font-weight:700;color:var(--heading)}
.tip-cat{position:absolute;left:436px;font-size:12px;color:var(--link)}
.tip-cat.plain{color:#111}
.tip-title{position:absolute;left:437px;font-size:12px;font-weight:700;color:var(--text)}
.tip-meta{position:absolute;left:438px;font-size:11px;color:#555}
.tip-meta b{color:#111;font-weight:400;text-decoration:underline}
.stars{position:absolute;left:578px;font-size:13px;letter-spacing:1px;color:#5a7fc0}
.rated{position:absolute;left:654px;font-size:12px;color:#666}
.pdf{position:absolute;left:692px;width:44px;height:26px}

/* knowledge */
.intro{position:absolute;left:761px;top:491px;font-size:12px;font-weight:700;color:var(--text)}
.stats{position:absolute;left:765px;top:520px;list-style:none}
.stats li{font-size:13px;line-height:20.5px;font-weight:700;color:var(--heading);position:relative;padding-left:17px}
.stats li::before{content:"";position:absolute;left:1px;top:8px;width:5px;height:5px;border-radius:50%;background:var(--link)}
.stats b{display:inline-block;width:49px;color:#111}
.select{position:absolute;left:764px;top:626px;width:257px;height:31px;background:linear-gradient(#f4f2ec,#ddd8cc);border:1px solid var(--button-line);font-size:13px;font-weight:700;color:#555;padding:8px 10px}
.select svg{position:absolute;right:5px;top:7px}
.ok{left:1024px;top:625px;width:36px;height:33px;font-size:13px}
.popular{position:absolute;left:764px;top:661px;font-size:13px;font-weight:700;color:var(--text)}
.countries{position:absolute;left:764px;top:680px;width:310px;font-size:12px;line-height:20px;color:var(--link);word-spacing:0}
.countries a{margin-right:5px}

/* partners */
.rule{position:absolute;left:122px;width:950px;height:1px;background:var(--rule)}
.partner{position:absolute;top:814px;height:50px;display:flex;align-items:center;gap:7px;font-size:14px;font-weight:700;color:var(--partner);line-height:16px}
.partner i{display:block;width:14px;height:14px;background:#b0b0b0;flex:none}
</style>
</head>
<body>

<aside class="services">
  <ul>
    <li>Coprorate Law (975)</li>
    <li>Investment Promotion (817)</li>
    <li>Distributors (656)</li>
    <li>Tranlation (621)</li>
    <li>Debt Collection (561)</li>
    <li>Accounting Services (519)</li>
    <li>Expat Services (512)</li>
    <li>Market Research (512)</li>
    <li>Debt Collection (561)</li>
    <li>Freight Forwarders (7843)</li>
    <li>Trading Companies (2489)</li>
    <li>Coprorate Law (975)</li>
    <li>Investment Promotion (817)</li>
    <li>Distributors (656)</li>
    <li>Tranlation (621)</li>
    <li>Debt Collection (561)</li>
    <li>Accounting Services (519)</li>
    <li>Expat Services (512)</li>
    <li>Market Research (512)</li>
    <li>Debt Collection (561)</li>
    <li class="group-start">Freight Forwarders (7843)</li>
    <li>Trading Companies (2489)</li>
    <li>Coprorate Law (975)</li>
    <li>Investment Promotion (817)</li>
    <li>Distributors (656)</li>
    <li>Tranlation (621)</li>
    <li>Debt Collection (561)</li>
  </ul>
  <a class="all" href="#">View all services</a>
</aside>

<main class="panel"></main>

<!-- testimonials -->
<p class="quote" style="top:-3px">scing elit. Integer vehicula, lectus at laoreet gnissim.Lorem ipsum dolor sit amet, consectetur adipiscing elit. ula, lectus at laoreet dignissim.Lorem ipsum dolor sit amet, consectetur adipiscing elit. Integer vehicula, lectus at laoreet dignissim.orem ipsum dolor sit amet, consectetur adipiscing elit.orem ipsum dolor sit amet ”</p>
<div class="rule-h" style="left:407px;top:131px;width:333px"></div>

<div class="zone">
  <svg width="83" height="82" viewBox="0 0 83 82" class="abs" style="left:0;top:0"><path d="M0 0L83 82M83 0L0 82" stroke="#999" stroke-width="1"/></svg>
  <span>Zone image</span>
</div>
<div class="abs speaker-name">Name Of Speaker</div>
<div class="abs speaker-role">Sourcing Services</div>
<div class="abs speaker-place">Florida, The United States</div>
<p class="quote" style="top:233px">“ Lorem ipsum dolor sit amet, consectetur adipi-scing elit. Integer vehicula, lectus at laoreet gnissim.Lorem ipsum dolor sit amet, consectetur adipiscing elit. ula, lectus at laoreet dignissim.Lorem ipsum dolor sit amet, consectetur adipiscing elit. Integer vehicula, lectus at laoreet dignissim.orem ipsum dolor sit amet, consectetur adipiscing elit.orem ipsum dolor sit amet”</p>
<a class="abs small-link" style="left:437px;top:401px" href="#">See the benefits</a>
<div class="btn" style="left:635px;top:388px;width:105px;height:39px">JOIN FOR FREE</div>

<!-- providers -->
<div class="card-logo" style="top:12px">Harbourline</div>
<div class="card-title" style="top:14px">Harbourline Trade Finance</div>
<div class="card-sub" style="top:30px">Factoring in the Unitated States</div>
<div class="card-desc" style="top:49px">Lorem ipsum dolor sit amet, consectetur adipiscing elit dolo lectus at laoreet...</div>
<a class="card-profile small-link" style="top:83px" href="#">View profile</a>

<div class="card-logo" style="top:122px;font-size:14px">EMF</div>
<div class="card-title" style="top:124px">Eastvale Materials Federation</div>
<div class="card-sub" style="top:140px">Professional Associacion in China</div>
<div class="card-desc" style="top:159px">Lorem ipsum dolor sit amet, consectetur adipiscing elit dolo lectus at laoreet...</div>
<a class="card-profile small-link" style="top:193px" href="#">View profile</a>

<div class="card-logo" style="top:232px">Tradewick</div>
<div class="card-title" style="top:234px">Tradewick Partners</div>
<div class="card-sub" style="top:250px">Professional Associacion in China</div>
<div class="card-desc" style="top:269px">Lorem ipsum dolor sit amet, consectetur adipiscing elit dolo lectus at laoreet...</div>
<a class="card-profile small-link" style="top:303px" href="#">View profile</a>

<p class="free" style="top:335px">It’s free to list your services on brindlework.net!</p>
<a class="abs small-link" style="left:773px;top:418px" href="#">See the benefits</a>
<div class="btn btn-cta" style="left:934px;top:389px;width:133px;height:39px">LIST YOUR SERVICES</div>
<svg class="abs" style="left:1034px;top:414px" width="20" height="26" viewBox="0 0 20 26"><path d="M6 2c1 0 2 1 2 2v7l1-1c1 0 2 1 2 1 1 0 2 1 2 1 1 0 2 1 2 2v6c0 2-1 4-3 5H8c-1-1-3-3-4-5l-2-3c-1-1 0-2 1-2l2 2V4c0-1 0-2 1-2z" fill="#fff" stroke="#333" stroke-width="1"/></svg>

<div class="rule-h" style="left:407px;top:435px;width:668px"></div>

<!-- business tips -->
<h2 class="section-title" style="left:495px;top:455px">Business Tips By Experts</h2>

<div class="tip-cat" style="top:485px">Business administration</div>
<div class="tip-title" style="top:499px">Lorem ipsum dolor sit amet, consectetur</div>
<div class="tip-meta" style="top:514px"><b>a law update</b> by Lorem Ipsum</div>
<div class="stars" style="top:531px">★★★</div>
<div class="rated" style="top:533px">Rated</div>
<svg class="pdf" style="top:527px" viewBox="0 0 44 26"><path d="M20 1h16l6 6v18H20z" fill="#fff" stroke="#777"/><rect x="1" y="5" width="32" height="14" fill="#3f78c4"/><text x="17" y="15.5" font-size="9" font-family="Arimo,Arial,sans-serif" fill="#fff" text-anchor="middle">PDF</text></svg>

<div class="tip-cat" style="top:559px">Business administration</div>
<div class="tip-title" style="top:573px">Lorem ipsum dolor sit amet, consectetur</div>
<div class="tip-meta" style="top:588px"><b>a law update</b> by Lorem Ipsum</div>
<div class="stars" style="top:605px">★★★</div>
<div class="rated" style="top:607px">Rated</div>
<svg class="pdf" style="top:601px" viewBox="0 0 44 26"><path d="M20 1h16l6 6v18H20z" fill="#fff" stroke="#777"/><rect x="1" y="5" width="32" height="14" fill="#3f78c4"/><text x="17" y="15.5" font-size="9" font-family="Arimo,Arial,sans-serif" fill="#fff" text-anchor="middle">PDF</text></svg>

<div class="tip-cat plain" style="top:636px">Business administration</div>
<div class="tip-title" style="top:651px">Lorem ipsum dolor sit amet, consectetur</div>
<div class="tip-meta" style="top:665px"><b>a law update</b> by Lorem Ipsum</div>
<div class="stars" style="top:682px">★★★</div>
<div class="rated" style="top:684px">Rated</div>
<svg class="pdf" style="top:678px" viewBox="0 0 44 26"><path d="M20 1h16l6 6v18H20z" fill="#fff" stroke="#777"/><rect x="1" y="5" width="32" height="14" fill="#3f78c4"/><text x="17" y="15.5" font-size="9" font-family="Arimo,Arial,sans-serif" fill="#fff" text-anchor="middle">PDF</text></svg>

<a class="abs small-link" style="left:438px;top:723px" href="#">Browse all content</a>
<div class="btn" style="left:637px;top:710px;width:97px;height:30px">RECEIVE UPDATES</div>

<!-- knowledge resource -->
<h2 class="section-title" style="left:805px;top:452px">Knowledge Resource</h2>
<p class="intro">Find resources for your business amongst:</p>
<ul class="stats">
  <li><b>10,145</b> market analyses</li>
  <li><b>9,254</b> business tips</li>
  <li><b>3,215</b> agents and distributors</li>
  <li><b>50,145</b> service providers</li>
</ul>
<div class="select">Select a Country
  <svg width="17" height="16" viewBox="0 0 17 16"><rect x=".5" y=".5" width="16" height="15" fill="#fff" stroke="#999"/><path d="M4 5h9l-4.5 6z" fill="#555"/></svg>
</div>
<div class="btn ok">OK</div>
<p class="popular">Most popular:</p>
<p class="countries">
  <a href="#">China</a>, <a href="#">Brazil</a>, <a href="#">Japan</a>, <a href="#">India</a>, <a href="#">Egypt</a>, <a href="#">Korea</a>, <a href="#">Angola</a>,
  <a href="#">Italy</a>, <a href="#">Englad</a>, <a href="#">Romania</a>, <a href="#">Spain</a>, <a href="#">Argentina</a>, <a href="#">France</a>,
  <a href="#">China</a>, <a href="#">Brazil</a>, <a href="#">Japan</a>, <a href="#">India</a>, <a href="#">Egypt</a>, <a href="#">Korea</a>, <a href="#">Angola</a>
</p>

<!-- partners -->
<div class="rule" style="top:777px"></div>
<div class="partner" style="left:135px"><i></i>Northgate<br>Commerce</div>
<div class="partner" style="left:240px"><i></i>Pellham<br>Council</div>
<div class="partner" style="left:360px;font-size:16px">Orvella</div>
<div class="partner" style="left:572px"><i></i>Lumen Federation</div>
<div class="partner" style="left:737px;font-size:16px">Corveth Net</div>
<div class="partner" style="left:912px"><i></i>Ashmere<br>Trade Office</div>
<div class="rule" style="top:893px"></div>

</body>
</html>
```